KORBLE Development is an idea development firm. This business card is for Weekend Wicket League, a site that allows users from all over the world to play fantasy cricket against each other.
We need a business card for WWL using our logo and its associated colors. The cards are for the two founders, Tobias Whitlow and Martin Dobrescu. We would like our own cards.
We are handing our card to potential investors and sponsors of our site. It needs to be unique (like our brand.)
Updates
I wanted to thank everyone for their awesome designs!!! It was a hard choice - we narrowed it down to 7 then to three then to 1. All of you are extremely talented - THANK YOU.
Target Market(s)
Potential Investors, Partners
Industry/Entity Type
Business
Contact Information for Business Card
Korble Development : Weekend Wicket League
Tobias Whitlow
Founder
555-204-7316
tobias@korble.example
www.weekendwicketleague.example
....
Martin Dobrescu
Founder
555-871-0492
martin@korble.example
Look and feel

```html
<!DOCTYPE html>
<html lang="en">
<head>
<meta charset="utf-8">
<title>Weekend Wicket League – Founder Cards</title>
<link rel="stylesheet" href="https://fonts.googleapis.com/css2?family=Ubuntu:wght@500;700&display=swap">
<style>
  :root {
    --field: #bfe07a;
    --lime-light: #d9ea2a;
    --lime-deep: #79c53a;
    --royal: #1d5fb5;
    --royal-deep: #1a49a4;
    --badge: #2a9a3e;
    --ink-white: #ffffff;
    --ink-navy: #343d86;
  }
  html, body {
    margin: 0;
    padding: 0;
    width: 1057px;
    height: 1200px;
    overflow: hidden;
    background: var(--field);
  }
  .sheet {
    display: block;
    width: 1057px;
    height: 1200px;
  }
  .holder-name {
    font-family: "Ubuntu", sans-serif;
    font-weight: 700;
    font-size: 46px;
    fill: var(--ink-white);
  }
  .holder-role {
    font-family: "Ubuntu", sans-serif;
    font-weight: 500;
    font-size: 24px;
    fill: var(--ink-navy);
  }
  .contact-line {
    font-family: "Ubuntu", sans-serif;
    font-weight: 700;
    font-size: 21px;
    fill: var(--ink-white);
    letter-spacing: 0.5px;
  }
  .brand-name {
    font-family: "Ubuntu", sans-serif;
    font-weight: 500;
    font-size: 17px;
    fill: var(--ink-white);
  }
  .brand-tile { fill: var(--badge); }
  .stripe-lime { fill: url(#stripeLime); }
  .stripe-royal { fill: url(#stripeRoyal); }
  .band-lime { fill: url(#bandLime); }
  .band-royal { fill: url(#bandRoyal); }
</style>
</head>
<body>
<svg class="sheet" viewBox="0 0 970 1100" preserveAspectRatio="none" xmlns="http://www.w3.org/2000/svg">
  <defs>
    <linearGradient id="stripeLime" x1="0" y1="0" x2="0" y2="1">
      <stop offset="0" stop-color="#b8e04a"/>
      <stop offset="0.7" stop-color="#a8d63e"/>
      <stop offset="1" stop-color="#7f8a2c"/>
    </linearGradient>
    <linearGradient id="stripeRoyal" x1="0" y1="0" x2="0" y2="1">
      <stop offset="0" stop-color="#1f5bb5"/>
      <stop offset="1" stop-color="#1b4a98"/>
    </linearGradient>
    <linearGradient id="bandLime" x1="0" y1="0" x2="0" y2="1">
      <stop offset="0" stop-color="#dde82a"/>
      <stop offset="0.45" stop-color="#8fd03c"/>
      <stop offset="1" stop-color="#6fc23a"/>
    </linearGradient>
    <linearGradient id="bandRoyal" x1="0" y1="0" x2="0" y2="1">
      <stop offset="0" stop-color="#1f6ac2"/>
      <stop offset="1" stop-color="#1a45a0"/>
    </linearGradient>
    <filter id="lift" x="-10%" y="-20%" width="120%" height="150%">
      <feDropShadow dx="1" dy="2" stdDeviation="1.5" flood-color="#3d5a12" flood-opacity="0.55"/>
    </filter>
  </defs>

  <!-- Card: Tobias Whitlow -->
  <g class="card card-tobias">
    <rect class="stripe-lime" x="82" y="0" width="53" height="332"/>
    <rect class="stripe-royal" x="136" y="0" width="54" height="332"/>
    <rect class="stripe-lime" x="191" y="0" width="53" height="332"/>

    <polygon class="band-lime" points="82,332 970,332 970,382 132,382"/>
    <polygon class="band-royal" points="136,389 970,389 970,438 185,438"/>
    <polygon class="band-lime" points="190,446 970,446 970,496 238,496"/>

    <g class="brand-mark">
      <rect class="brand-tile" x="392" y="70" width="138" height="140"/>
      <text class="brand-name" x="461" y="125" text-anchor="middle">Weekend</text>
      <text class="brand-name" x="461" y="147" text-anchor="middle">Wicket</text>
      <text class="brand-name" x="461" y="169" text-anchor="middle">League</text>
    </g>

    <text class="holder-name" x="557" y="177" filter="url(#lift)">Tobias Whitlow</text>
    <text class="holder-role" x="625" y="210">Founder</text>

    <text class="contact-line" x="668" y="364" text-anchor="middle" filter="url(#lift)">555-204-7316</text>
    <text class="contact-line" x="670" y="421" text-anchor="middle" filter="url(#lift)">tobias@korble.example</text>
    <text class="contact-line" x="670" y="478" text-anchor="middle" filter="url(#lift)">www.weekendwicketleague.example</text>
  </g>

  <!-- Card: Martin Dobrescu -->
  <g class="card card-martin">
    <rect class="stripe-lime" x="82" y="572" width="53" height="308"/>
    <rect class="stripe-royal" x="136" y="572" width="54" height="308"/>
    <rect class="stripe-lime" x="191" y="572" width="53" height="308"/>

    <polygon class="band-lime" points="82,880 970,880 970,925 128,925"/>
    <polygon class="band-royal" points="136,932 970,932 970,977 182,977"/>
    <polygon class="band-lime" points="190,985 970,985 970,1030 236,1030"/>

    <g class="brand-mark">
      <rect class="brand-tile" x="392" y="637" width="138" height="130"/>
      <text class="brand-name" x="461" y="687" text-anchor="middle">Weekend</text>
      <text class="brand-name" x="461" y="709" text-anchor="middle">Wicket</text>
      <text class="brand-name" x="461" y="731" text-anchor="middle">League</text>
    </g>

    <text class="holder-name" x="543" y="732" filter="url(#lift)" style="font-size:40px">Martin Dobrescu</text>
    <text class="holder-role" x="625" y="767">Founder</text>

    <text class="contact-line" x="676" y="909" text-anchor="middle" filter="url(#lift)">555-871-0492</text>
    <text class="contact-line" x="676" y="962" text-anchor="middle" filter="url(#lift)">martin@korble.example</text>
    <text class="contact-line" x="670" y="1014" text-anchor="middle" filter="url(#lift)">www.weekendwicketleague.example</text>
  </g>
</svg>
</body>
</html>
```